Business card needed for home based pen making business.

I'm after a business card that's a bit more than an off the shelf card. I do like the idea of a card split horizontal with different colours used. A third colour is to be used for the business name and if need a forth for the other details.

I don't have a logo and will pay extra for one ($150 extra). I mainly make pens and seam rippers (stitch unpicks). The logo may be used for a website in future, as will the colours so please provide the colour codes and font type.

I'd like the business name in an easy to read script font at the top (with logo if you have one) and the other details to the bottom left hand side. I'll leave it up to you to match the script to the font used for the other details.

I'd like to keep a triangular balance to the card so something like a siloet of pot containing pens on the bottom right could be used to balance it out. There my ideas I want to see your.

Business name: Quillo & Co
Email address: quilloandco@mailvista.net
Contact: Dorian
Phone: 0418 352 976
No address is to be used on card.

Target Market(s)

Wide variety of people visiting craft markets. Age range 30+.

Industry/Entity Type

Business

Contact Information for Business Card

Quill & Co

Font styles to use
Script

Colors
f0ecf4
3277b5
3176b5

Requirements
Must have
• Contact: Dorian
• Phone: 0418 352 976
• Email address: quilloandco@mailvista.net
Nice to have
• An icon and/or graphics depicting pens and seam rippers..
Should not have
• I don't want icon/ graphic to be a crossed pen and seam ripper.

```html
<!DOCTYPE html>
<html lang="en">
<head>
<meta charset="utf-8">
<title>Quillo &amp; Co — Business Card</title>
<link rel="stylesheet" href="https://fonts.googleapis.com/css2?family=Open+Sans:wght@400;600&family=Arimo:wght@400&display=swap">
<style>
  :root {
    --backdrop: #f0ecf4;
    --card: #ffffff;
    --card-shade: #f2f2f3;
    --brand-blue: #3277b5;
    --band-blue: #3176b5;
    --band-black: #0a0a0a;
    --rule: #2b2b2b;
    --divider: #8a8a8a;
    --contact-ink: #222222;
    --wood-light: #b08a4e;
    --wood-dark: #7a5a2c;
  }
  html, body {
    margin: 0;
    padding: 0;
    width: 1200px;
    height: 902px;
    overflow: hidden;
    background: var(--backdrop);
  }
  .stage {
    width: 1200px;
    height: 902px;
    display: flex;
    align-items: center;
    justify-content: center;
  }
  .business-card {
    position: relative;
    width: 900px;
    height: 550px;
    background: linear-gradient(180deg, var(--card) 0%, var(--card-shade) 100%);
    box-shadow: 0 10px 30px rgba(0,0,0,0.18);
    overflow: hidden;
  }
  .business-name {
    position: absolute;
    left: 58px;
    top: 92px;
    margin: 0;
    font-family: "Open Sans", sans-serif;
    font-weight: 400;
    font-size: 84px;
    letter-spacing: 1px;
    color: var(--brand-blue);
    line-height: 1;
  }
  .name-rule {
    position: absolute;
    left: 420px;
    top: 214px;
    width: 290px;
    height: 2px;
    background: var(--rule);
  }
  .contact-person {
    position: absolute;
    left: 720px;
    top: 168px;
    font-family: "Open Sans", sans-serif;
    font-weight: 600;
    font-size: 40px;
    color: var(--brand-blue);
    line-height: 1;
  }
  .product-photo {
    position: absolute;
    left: 560px;
    top: 238px;
    width: 300px;
    height: 44px;
    border-radius: 22px;
    background: linear-gradient(180deg, var(--wood-light) 0%, var(--wood-dark) 100%);
  }
  .section-divider {
    position: absolute;
    left: 0;
    top: 318px;
    width: 100%;
    height: 1.5px;
    background: var(--divider);
  }
  .contact-details {
    position: absolute;
    left: 58px;
    top: 368px;
    font-family: "Arimo", sans-serif;
    font-size: 25px;
    color: var(--contact-ink);
    line-height: 1.55;
  }
  .contact-details p { margin: 0; }
  .colour-bands {
    position: absolute;
    left: 0;
    top: 0;
    width: 900px;
    height: 550px;
  }
  .band-blue { fill: var(--band-blue); }
  .band-black { fill: var(--band-black); }
</style>
</head>
<body>
<main class="stage">
  <article class="business-card">
    <svg class="colour-bands" viewBox="0 0 900 550" aria-hidden="true">
      <path class="band-blue" d="M0 472 H572 L552 550 H0 Z"/>
      <path class="band-black" d="M900 332 V550 H556 L588 478 Q600 452 632 452 H760 Q790 452 810 430 Z"/>
    </svg>

    <h1 class="business-name">Quillo &amp; Co</h1>
    <div class="name-rule"></div>
    <span class="contact-person">Dorian</span>

    <div class="product-photo" role="img" aria-label="Photo of a handmade wooden seam ripper with brass fittings"></div>

    <div class="section-divider"></div>

    <div class="contact-details">
      <p class="phone">0418 352 976</p>
      <p class="email">quilloandco@mailvista.net</p>
    </div>
  </article>
</main>
</body>
</html>
```